Business Card Design Project

Fernwick Pediatric Dentistry is a, kids dental office, located in prestigious Georgetown Washington DC, just blocks from the copper hall. We are fee for service office that has great patients who value their dental care.

I have attached our logo files in black and white, we would like our logo on our cards as well.

```html
<!DOCTYPE html>
<html lang="en">
<head>
<meta charset="utf-8">
<title>Fernwick Pediatric Dentistry – Business Cards</title>
<link rel="stylesheet" href="https://fonts.googleapis.com/css2?family=Cinzel:wght@400&family=Lato:wght@400&display=swap">
<style>
  :root {
    --backdrop: #4a4849;
    --card: #ffffff;
    --ink: #111111;
    --shadow: rgba(0, 0, 0, 0.45);
  }
  html, body {
    margin: 0;
    padding: 0;
    width: 1200px;
    height: 858px;
    overflow: hidden;
    background: var(--backdrop);
  }
  .canvas {
    position: relative;
    width: 1200px;
    height: 858px;
  }
  .card {
    position: absolute;
    width: 540px;
    height: 310px;
    background: var(--card);
    box-shadow: 0 10px 28px var(--shadow);
    color: var(--ink);
  }
  .card--front { left: 70px; top: 130px; }
  .card--back { left: 590px; top: 420px; }

  .wordmark {
    font-family: "Cinzel", serif;
    font-weight: 400;
    color: var(--ink);
    text-align: center;
    line-height: 1.05;
    margin: 0;
  }
  .wordmark__main { display: block; letter-spacing: 0.02em; }
  .wordmark__sub { display: block; letter-spacing: 0.06em; }

  .card--front .wordmark {
    position: absolute;
    left: 0; right: 0;
    top: 118px;
  }
  .card--front .wordmark__main { font-size: 44px; }
  .card--front .wordmark__sub { font-size: 17px; margin-top: 4px; }

  .card--back .wordmark {
    position: absolute;
    right: 34px;
    top: 32px;
  }
  .card--back .wordmark__main { font-size: 27px; }
  .card--back .wordmark__sub { font-size: 10.5px; margin-top: 2px; }

  .person {
    position: absolute;
    left: 40px;
    top: 120px;
  }
  .person__name {
    font-family: "Cinzel", serif;
    font-size: 25px;
    font-weight: 400;
    margin: 0;
    letter-spacing: 0.02em;
  }
  .person__role {
    font-family: "Lato", sans-serif;
    font-size: 14px;
    margin: 2px 0 0;
  }

  .address {
    position: absolute;
    left: 40px;
    top: 196px;
    font-family: "Lato", sans-serif;
    font-style: normal;
    font-size: 13.5px;
    line-height: 1.35;
  }

  .contact {
    position: absolute;
    left: 40px;
    top: 240px;
    margin: 0;
    padding: 0;
    list-style: none;
    font-family: "Lato", sans-serif;
    font-size: 13.5px;
    line-height: 1.4;
  }
  .contact__item {
    display: flex;
    align-items: center;
    gap: 9px;
  }
  .contact__icon { width: 11px; height: 11px; fill: var(--ink); }
</style>
</head>
<body>
<main class="canvas">

  <section class="card card--front" aria-label="Card front">
    <p class="wordmark">
      <span class="wordmark__main">FERNWICK</span>
      <span class="wordmark__sub">PEDIATRIC DENTISTRY</span>
    </p>
  </section>

  <section class="card card--back" aria-label="Card back">
    <p class="wordmark">
      <span class="wordmark__main">FERNWICK</span>
      <span class="wordmark__sub">PEDIATRIC DENTISTRY</span>
    </p>

    <div class="person">
      <h1 class="person__name">MARCUS HALE</h1>
      <p class="person__role">Founder &amp; CEO</p>
    </div>

    <address class="address">
      Suite 410, 18 Ashcombe Road<br>
      Georgetown Washington DC
    </address>

    <ul class="contact">
      <li class="contact__item">
        <svg class="contact__icon" viewBox="0 0 12 12" aria-hidden="true"><path d="M2.5 0.5l2 2.2-1 1.3c.7 1.6 1.9 2.8 3.5 3.5l1.3-1 2.2 2-1.2 1.8C5 10 1.9 6.9 0.7 1.7z"/></svg>
        <span>202 555 0148</span>
      </li>
      <li class="contact__item">
        <svg class="contact__icon" viewBox="0 0 12 12" aria-hidden="true"><path d="M0.5 2.5h11v7h-11z M0.5 2.5l5.5 4 5.5-4" fill="none" stroke="#111" stroke-width="1.2"/><path d="M0.5 2.5h11L6 6.5z"/></svg>
        <span>info@fernwick.com</span>
      </li>
      <li class="contact__item">
        <svg class="contact__icon" viewBox="0 0 12 12" aria-hidden="true"><circle cx="6" cy="6" r="5.5"/><path d="M0.5 6h11M6 0.5c-2.5 3-2.5 8 0 11M6 0.5c2.5 3 2.5 8 0 11" fill="none" stroke="#fff" stroke-width="0.8"/></svg>
        <span>www.fernwick.com</span>
      </li>
    </ul>
  </section>

</main>
</body>
</html>
```